Popup-Fenster Design für Öffnungszeiten
Zielgruppe
Planung und Realisierung von individuellen Kaminen.
Aufgabenstellung
Für unsere Website www.lindenhaus-torvel.de benötigen wir ein Popup-Fenster für die Startseite. Da das Geschäft nicht jeden Tag und zu festen Zeit geöffnet hat, soll der Kunde direkt sehen können, wann das Geschäft das nächste Mal geöffnet hat. Das Popup-Fenster soll auffällig, jedoch nicht überladen und aufdringlich sein. Einen eigenen Entwurf (der mir nicht gefällt) habe ich hochgeladen. Vielleicht benötigt dieser nur noch einen Feinschliff!? Es muss nicht reckteckig sein, ich bin auch für runde oder ovale Formen offen. Der dort eingesetzte Text sollte als Platzhalter eingesetzt werden. Bei Fragen können Sie mir gerne eine Nachricht zukommen lassen.

```html
<!DOCTYPE html>
<html lang="de">
<head>
<meta charset="utf-8">
<title>Lindenhaus – Öffnungszeiten Popup</title>
<link href="https://fonts.googleapis.com/css2?family=Raleway:wght@200;300;400&family=Roboto+Condensed:wght@400;700&family=Playfair+Display:ital@1&display=swap" rel="stylesheet">
<style>
  :root {
    --canvas-bg: #ffffff;
    --sidebar-bg: #232323;
    --sidebar-text: #4a4a48;
    --brand-gold: #6f6444;
    --photo-dark: #2e2f31;
    --photo-mid: #4b4d50;
    --photo-light: #6a6b6c;
    --hero-text: #8a8a8a;
    --popup-bg: #1f1f1e;
    --popup-gold: #c9b47a;
    --popup-title: #dcc57c;
    --popup-text: #f2e3a6;
  }
  * { margin: 0; padding: 0; box-sizing: border-box; }
  html, body {
    width: 1109px; height: 1200px; overflow: hidden;
    background: var(--canvas-bg);
  }
  .screen {
    position: absolute; left: 50px; top: 359px;
    width: 1009px; height: 482px;
    overflow: hidden;
    font-family: "Raleway", sans-serif;
  }
  .sidebar {
    position: absolute; left: 0; top: 0;
    width: 222px; height: 100%;
    background: var(--sidebar-bg);
  }
  .brand {
    position: absolute; left: 0; right: 0; top: 94px;
    text-align: center;
    font-family: "Raleway", sans-serif; font-weight: 300;
    font-size: 12px; letter-spacing: 5px;
    color: var(--brand-gold);
  }
  .brand-mark {
    display: block; width: 44px; height: 44px;
    margin: -60px auto 14px;
    border: 2px solid var(--brand-gold);
  }
  .nav { position: absolute; left: 37px; top: 188px; list-style: none; }
  .nav li {
    font-weight: 300; font-size: 13px; height: 38.5px;
    color: var(--sidebar-text); text-transform: uppercase;
  }
  .legal {
    position: absolute; left: 37px; bottom: 18px;
    font-size: 8px; color: #3d3d3b;
  }
  .hero-photo {
    position: absolute; left: 222px; top: 0; right: 0; bottom: 0;
    background:
      linear-gradient(180deg, #3a3a38 0%, #3a3a38 8%, transparent 8%),
      linear-gradient(180deg, var(--photo-mid) 10%, var(--photo-light) 45%, var(--photo-mid) 62%, var(--photo-dark) 100%);
  }
  .hero-title {
    position: absolute; left: 257px; top: 190px;
    font-weight: 200; font-size: 44px; letter-spacing: 1px;
    color: var(--hero-text); white-space: nowrap;
  }
  .hero-sub {
    position: absolute; left: 650px; top: 240px;
    font-family: "Playfair Display", serif; font-style: italic;
    font-size: 26px; color: #6e6e6c;
  }
  .hero-cta {
    position: absolute; left: 520px; top: 428px;
    font-size: 10px; letter-spacing: 1px; color: #5b5b59;
  }
  .popup { position: absolute; left: 0; top: 0; }
  .popup text { font-family: "Roboto Condensed", sans-serif; }
</style>
</head>
<body>
  <div class="screen">
    <aside class="sidebar">
      <div class="brand"><span class="brand-mark"></span>LINDENHAUS</div>
      <ul class="nav">
        <li>Über uns</li>
        <li>Kaminöfen</li>
        <li>Holzkamine</li>
        <li>Gaskamine</li>
        <li>Ausstellung</li>
        <li>Kontakt</li>
      </ul>
      <div class="legal">Impressum | Datenschutz</div>
    </aside>

    <div class="hero-photo" role="img" aria-label="Abgedunkeltes Foto: Raum mit Panoramafenstern über Berglandschaft und hängendem Kamin"></div>
    <div class="hero-title">WILLKOMMEN IM LINDENHAUS</div>
    <div class="hero-sub">Wärme erleben</div>
    <div class="hero-cta">Jetzt Beratungstermin vereinbaren</div>

    <svg class="popup" width="1009" height="482" viewBox="0 0 1009 482">
      <ellipse cx="505" cy="240" rx="142" ry="106" fill="var(--popup-bg)" stroke="var(--popup-gold)" stroke-width="3"/>
      <circle cx="599" cy="161" r="15" fill="var(--popup-bg)" stroke="var(--popup-gold)" stroke-width="3"/>
      <path d="M593 155 L605 167 M605 155 L593 167" stroke="#ffffff" stroke-width="2.5" stroke-linecap="round"/>
      <text x="505" y="210" text-anchor="middle" font-size="23" fill="var(--popup-title)">ÖFFNUNGSZEITEN</text>
      <text x="505" y="237" text-anchor="middle" font-size="13.5" font-weight="700" fill="var(--popup-text)">Wir haben für Sie geöffnet:</text>
      <text x="505" y="256" text-anchor="middle" font-size="9.5" fill="var(--popup-text)">Fr 17.01 14:00 - 17:00 Uhr</text>
      <text x="505" y="268" text-anchor="middle" font-size="9.5" fill="var(--popup-text)">Sa 18.01 10:00 - 13:00 Uhr</text>
      <text x="505" y="290" text-anchor="middle" font-size="9.5" fill="var(--popup-text)">Weitere Termine ansehen</text>
      <text x="505" y="301" text-anchor="middle" font-size="9.5" fill="var(--popup-text)">Individuellen Termin vereinbaren</text>
    </svg>
  </div>
</body>
</html>
```